Aunt Rolina's Bakery

I am about to create a luxury boutique that specializes in cake baking and cupcake
and ready for parties and special events and order delivery
the logo has already made

Industry/Entity Type

Boutique

Contact Information for Business Card

Email:auntrolinasbakery@maplecrumbmail.com
Instagram: aunt_rolina_bakery
Twitter: xxxxxxx
WhatsApp: xxxxxxx

Requirements
Must have
• luxury design

```html
<!DOCTYPE html>
<html lang="en">
<head>
<meta charset="utf-8">
<title>Aunt Rolina's Bakery – Business Card</title>
<link rel="stylesheet" href="https://fonts.googleapis.com/css2?family=Lato:wght@400;700&display=swap">
<style>
  :root {
    --stage: #ecebe8;
    --card: #ffffff;
    --card-shade: #f4f4f3;
    --stone: #8f8e88;
    --stone-line: #b3b2ac;
    --rose: #e4a9bb;
    --rose-text: #e08fa9;
    --ink: #8a8985;
    --on-stone: #ffffff;
  }
  * { margin: 0; padding: 0; box-sizing: border-box; }
  html, body {
    width: 1200px; height: 780px; overflow: hidden;
    background: var(--stage);
    font-family: "Lato", Arial, sans-serif;
  }
  .canvas {
    position: relative; width: 1200px; height: 780px;
    display: flex; align-items: center; justify-content: center;
  }
  .card {
    position: relative; width: 1050px; height: 600px;
    background: linear-gradient(135deg, var(--card) 0%, var(--card-shade) 100%);
    box-shadow: 0 14px 40px rgba(60, 55, 45, 0.18);
    overflow: hidden;
  }
  .card__waves { position: absolute; inset: 0; width: 100%; height: 100%; }

  .brand {
    position: absolute; left: 60px; top: 205px;
    display: flex; align-items: center; gap: 20px;
  }
  .brand__dot {
    width: 54px; height: 54px; border-radius: 50%; flex: none;
    background: var(--rose);
  }
  .brand__name {
    font-weight: 400; font-size: 34px; letter-spacing: 3px;
    color: var(--ink); text-transform: uppercase; line-height: 1.15;
  }

  .person {
    position: absolute; left: 300px; top: 58px;
  }
  .person__name {
    font-weight: 700; font-size: 42px; color: var(--ink); letter-spacing: 0.5px;
    line-height: 1.2;
  }
  .person__role {
    font-weight: 400; font-size: 24px; color: var(--rose-text);
    margin-top: 2px; margin-left: 70px;
  }

  .contacts {
    position: absolute; right: 42px; top: 200px;
    list-style: none; display: flex; flex-direction: column; gap: 10px;
  }
  .contacts__item {
    display: flex; align-items: center; justify-content: flex-end; gap: 14px;
    font-size: 21px; color: var(--on-stone); letter-spacing: 0.2px;
  }
  .contacts__icon { width: 22px; height: 22px; flex: none; }
</style>
</head>
<body>
<main class="canvas">
  <article class="card">
    <svg class="card__waves" viewBox="0 0 1050 600" preserveAspectRatio="none" aria-hidden="true">
      <path d="M330 600 C 400 450, 420 350, 520 260 C 600 190, 680 120, 720 0 L 1050 0 L 1050 600 Z" fill="var(--stone)"/>
      <path d="M210 600 C 300 520, 370 450, 400 380 C 380 470, 330 550, 290 600 Z" fill="var(--rose)"/>
      <path d="M280 600 C 360 500, 390 400, 470 320 C 410 420, 370 520, 310 600 Z" fill="var(--stone-line)"/>
    </svg>

    <div class="brand">
      <span class="brand__dot"></span>
      <h1 class="brand__name">Aunt Rolina's<br>Bakery</h1>
    </div>

    <header class="person">
      <h2 class="person__name">Employee Name</h2>
      <p class="person__role">Managing Director</p>
    </header>

    <ul class="contacts">
      <li class="contacts__item">000.000.0000
        <svg class="contacts__icon" viewBox="0 0 24 24" aria-label="Phone"><path d="M6 3h4l1.5 5-2.5 1.5a11 11 0 0 0 5.5 5.5L16 12.5l5 1.5v4a2 2 0 0 1-2 2A16 16 0 0 1 4 5a2 2 0 0 1 2-2z" fill="var(--on-stone)"/></svg>
      </li>
      <li class="contacts__item">auntrolinasbakery@maplecrumbmail.com
        <svg class="contacts__icon" viewBox="0 0 24 24" aria-label="Email"><rect x="2" y="5" width="20" height="14" rx="1.5" fill="var(--on-stone)"/><path d="M3 6l9 7 9-7" stroke="var(--stone)" stroke-width="1.8" fill="none"/></svg>
      </li>
      <li class="contacts__item">aunt_rolina_bakery
        <svg class="contacts__icon" viewBox="0 0 24 24" aria-label="Social profile"><circle cx="12" cy="12" r="9" fill="var(--on-stone)"/></svg>
      </li>
      <li class="contacts__item">aunt_rolina_bakery
        <svg class="contacts__icon" viewBox="0 0 24 24" aria-label="Social profile"><circle cx="12" cy="12" r="9" fill="var(--on-stone)"/></svg>
      </li>
      <li class="contacts__item">aunt_rolina_bakery
        <svg class="contacts__icon" viewBox="0 0 24 24" aria-label="Messaging"><circle cx="12" cy="12" r="9" fill="var(--on-stone)"/></svg>
      </li>
    </ul>
  </article>
</main>
</body>
</html>
```